New Board Game - KZ 45:35:20

The project is in two phases:
A. GAME BOARD DESIGN
Design of a striking game board.
NB. See the following files:
* KZ 45:35:20 Background Info
* KZ 45:35:20 Game Board Format
NB. The contest fee is for Phase A only. Additional fees will be paid for Phase B.
B. APPLICATION OF GAME BOARD DESIGN
The game board design will to be applied to the following game materials:
* Game cards (front and back)
* Sticker for game board tube
* Facilitator's Handbook front and back cover
* Icon for pages inside Facilitator's Handbook
Additional information on the game cards will be provided to the winning designer.
Updates
Please note that the project fee is for Phase A only. We will pay additional fees for Phase B, i.e. game cards etc.
NOTE:
Please keep in mind that the game will be used in a corporate setting. The initial target group are Learning and Development (L&D) specialists, mainly people who develop or deliver training courses. They are all educated professionals.
I recently included this feedback in a message to one of the designers:
The game board has to have a level of sophistication and elegance that suits a corporate environment. The game will also be the first direct contact that some potential members will have with the Guild and has to make a positive impression on them.
We want people to perceive the game as a top-class, creative product.
PLEASE NOTE:
The project fee is now a guaranteed payment.
Target Market(s)
The game will initially be used at networking events held by the Halvern Guild of Practitioners in Australia (see: www.halverncircle.example). These events are attended by members and guests, with the group ranging from 10 to 20 attendees.
The game may also be used as part of management or leadership development programs in business and government organisations.
Another possible use is with teachers at networking events or professional development courses.
Requirements
Must have
- See the uploaded files for important design requirements.
What is most important is that the game materials are attractive, appealing, impactful. People (in the target group) who see the game materials should feel that they want to find out more, pick up the cards and play the game.
Should not have
- Still thinking....

```html
<!DOCTYPE html>
<html lang="en">
<head>
<meta charset="utf-8">
<title>KZ 45:35:20 – Game Board</title>
<link href="https://fonts.googleapis.com/css2?family=Bangers&family=Source+Sans+3:wght@400;700;900&display=swap" rel="stylesheet">
<style>
  :root {
    --page: #ffffff;
    --board-edge: #8cc63f;
    --navy: #0b2a6e;
    --logo-navy: #0a1a6b;
    --field-green: #5fa82a;
    --track: #ffffff;
    --corner-red: #d3201b;
    --corner-word: #ff8a1a;
    --orange-top: #ffa31a;
    --orange-bottom: #ec4612;
    --green-top: #a5d62a;
    --green-bottom: #5ea61b;
    --blue-top: #33c8f7;
    --blue-bottom: #0a8ee2;
    --yellow: #ffc520;
    --ink: #1a1a1a;
    --band-light: #9a9a9a;
    --band-dark: #6f6f6f;
  }
  * { box-sizing: border-box; margin: 0; padding: 0; }
  html, body { width: 1200px; height: 900px; overflow: hidden; background: var(--page); }
  .canvas { position: relative; width: 1200px; height: 900px; background: var(--page); font-family: "Source Sans 3", Arial, sans-serif; }

  .board {
    position: absolute; left: 198px; top: 50px; width: 836px; height: 720px;
    border: 8px solid var(--board-edge);
    background: linear-gradient(45deg, var(--navy) 0%, var(--field-green) 40%, var(--field-green) 55%, var(--navy) 100%);
    overflow: hidden;
  }
  .board__track { position: absolute; left: 0; top: 0; }

  .tile {
    position: absolute; width: 66px; height: 74px;
    border: 3px solid var(--track); border-radius: 6px;
    display: flex; align-items: center; justify-content: center;
    color: #fff; font-weight: 700; font-size: 27px; letter-spacing: -0.5px;
  }
  .tile--side { width: 76px; height: 66px; }
  .tile--orange { background: linear-gradient(160deg, var(--orange-top), var(--orange-bottom)); }
  .tile--green  { background: linear-gradient(160deg, var(--green-top), var(--green-bottom)); }
  .tile--blue   { background: linear-gradient(160deg, var(--blue-top), var(--blue-bottom)); }
  .tile--yellow { background: var(--yellow); }
  .tile__value sup { font-size: 11px; vertical-align: 12px; margin-left: 1px; }
  .tile__action {
    width: 44px; height: 44px; border: 2px solid var(--ink); border-radius: 50%;
    display: flex; flex-direction: column; align-items: center; justify-content: center;
    color: var(--ink); font-size: 11px; line-height: 1.05; font-weight: 700; text-align: center;
  }
  .tile--top .tile__value, .tile--top .tile__action { transform: rotate(180deg); }
  .tile--side .tile__value, .tile--side .tile__action { transform: rotate(90deg); }
  .tile--left .tile__value, .tile--left .tile__action { transform: rotate(90deg); }

  .corner-word {
    position: absolute; width: 140px; text-align: center;
    font-family: "Bangers", "Impact", sans-serif; font-size: 30px; line-height: 1;
    color: var(--corner-word); letter-spacing: 1px; white-space: nowrap;
  }

  .credit { position: absolute; font-size: 6.5px; color: #ffffff; white-space: nowrap; }
  .credit--bottom { left: 170px; top: 601px; }
  .credit--top { right: 148px; top: 96px; transform: rotate(180deg); }

  .game-title {
    position: absolute; left: 100px; top: 100px; width: 620px; height: 500px;
    display: flex; align-items: center; justify-content: center; gap: 16px;
  }
  .game-title__disc { width: 90px; height: 90px; border-radius: 50%; background: var(--logo-navy); flex: none; }
  .game-title__name { font-weight: 900; font-size: 56px; color: #ffffff; letter-spacing: -1px; white-space: nowrap; }

  .footer-band { position: absolute; left: 0; top: 788px; width: 1200px; height: 112px; background: linear-gradient(180deg, var(--band-light), var(--band-dark)); }
</style>
</head>
<body>
<div class="canvas">
  <section class="board" aria-label="KZ 45:35:20 game board">
    <svg class="board__track" width="820" height="704" viewBox="0 0 820 704" aria-hidden="true">
      <defs>
        <path id="corner-piece" d="M14 168 L14 80 Q14 8 86 8 L172 8 L172 90 L122 90 Q90 90 90 122 L90 168 Z"/>
      </defs>
      <rect x="47" y="52" width="726" height="599" rx="70" fill="none" stroke="#ffffff" stroke-width="82"/>
      <g fill="#d3201b" stroke="#ffffff" stroke-width="4">
        <use href="#corner-piece"/>
        <use href="#corner-piece" transform="translate(820,0) scale(-1,1)"/>
        <use href="#corner-piece" transform="translate(0,704) scale(1,-1)"/>
        <use href="#corner-piece" transform="translate(820,704) scale(-1,-1)"/>
      </g>
    </svg>

    <span class="corner-word" style="left:-8px;top:50px;transform:rotate(135deg);">YIKES!</span>
    <span class="corner-word" style="left:688px;top:50px;transform:rotate(-135deg);">OOPS!</span>
    <span class="corner-word" style="left:-8px;top:625px;transform:rotate(45deg);">UH-OH!</span>
    <span class="corner-word" style="left:688px;top:625px;transform:rotate(-45deg);">CRIKEY!</span>

    <!-- top row -->
    <div class="tile tile--top tile--green"  style="left:177px;top:15px;"><span class="tile__value">35<sup>%</sup></span></div>
    <div class="tile tile--top tile--yellow" style="left:249px;top:15px;"><span class="tile__action">ROLL<br>again</span></div>
    <div class="tile tile--top tile--orange" style="left:321px;top:15px;"><span class="tile__value">45<sup>%</sup></span></div>
    <div class="tile tile--top tile--orange" style="left:393px;top:15px;"><span class="tile__value">45<sup>%</sup></span></div>
    <div class="tile tile--top tile--orange" style="left:465px;top:15px;"><span class="tile__value">45<sup>%</sup></span></div>
    <div class="tile tile--top tile--yellow" style="left:537px;top:15px;"><span class="tile__action">ANY<br>card</span></div>
    <div class="tile tile--top tile--blue"   style="left:609px;top:15px;"><span class="tile__value">20<sup>%</sup></span></div>

    <!-- left column -->
    <div class="tile tile--side tile--green"  style="left:14px;top:177px;"><span class="tile__value">35<sup>%</sup></span></div>
    <div class="tile tile--side tile--blue"   style="left:14px;top:248px;"><span class="tile__value">20<sup>%</sup></span></div>
    <div class="tile tile--side tile--yellow" style="left:14px;top:320px;"><span class="tile__action">MISS<br>a turn</span></div>
    <div class="tile tile--side tile--orange" style="left:14px;top:392px;"><span class="tile__value">45<sup>%</sup></span></div>
    <div class="tile tile--side tile--orange" style="left:14px;top:463px;"><span class="tile__value">45<sup>%</sup></span></div>

    <!-- right column -->
    <div class="tile tile--side tile--green"  style="left:730px;top:177px;"><span class="tile__value">35<sup>%</sup></span></div>
    <div class="tile tile--side tile--green"  style="left:730px;top:248px;"><span class="tile__value">35<sup>%</sup></span></div>
    <div class="tile tile--side tile--yellow" style="left:730px;top:320px;"><span class="tile__action">MISS<br>a turn</span></div>
    <div class="tile tile--side tile--orange" style="left:730px;top:392px;"><span class="tile__value">45<sup>%</sup></span></div>
    <div class="tile tile--side tile--orange" style="left:730px;top:463px;"><span class="tile__value">45<sup>%</sup></span></div>

    <!-- bottom row -->
    <div class="tile tile--orange" style="left:177px;top:614px;"><span class="tile__value">45<sup>%</sup></span></div>
    <div class="tile tile--yellow" style="left:249px;top:614px;"><span class="tile__action">ANY<br>card</span></div>
    <div class="tile tile--green"  style="left:321px;top:614px;"><span class="tile__value">35<sup>%</sup></span></div>
    <div class="tile tile--green"  style="left:393px;top:614px;"><span class="tile__value">35<sup>%</sup></span></div>
    <div class="tile tile--blue"   style="left:465px;top:614px;"><span class="tile__value">20<sup>%</sup></span></div>
    <div class="tile tile--yellow" style="left:537px;top:614px;"><span class="tile__action">ROLL<br>again</span></div>
    <div class="tile tile--orange" style="left:609px;top:614px;"><span class="tile__value">45<sup>%</sup></span></div>

    <p class="credit credit--bottom">© Mara Velden, Halvern Guild of Practitioners &nbsp;www.halverncircle.example</p>
    <p class="credit credit--top">© Mara Velden, Halvern Guild of Practitioners &nbsp;www.halverncircle.example</p>

    <div class="game-title">
      <span class="game-title__disc" aria-hidden="true"></span>
      <h1 class="game-title__name">KZ 45:35:20</h1>
    </div>
  </section>

  <div class="footer-band" aria-hidden="true"></div>
</div>
</body>
</html>
```